Business Card Design Project : Tidewell Press

In preparation for market launch, Whistler's Tidewell Press require the development of a business card. Tidewell Press is a Community online publishing web portal. We provide the the city of Whistler located in B.C. (Canada) business directories, News, Classified ads, News, Events and blogs etc.

The main focus of the brand is to help local businesses to corporate with their online advertisement and marketing. Meeting our clients face to face is a must (B2B).

Target Market(s)

The target market is B2B customers. Business Owners to Marketing, advertising Managers

Industry/Entity Type

Business

Requirements
Must have
• - The business card will be two sided.
the BACK side will have our logo which consist of (icon, url,slogan) submited. The logo will be middle and centred.

The FRONT side should have company details:

Company Legal Name: FERNDALE TIDEWELL PRESS

Owen Marsk
Director of Sales & Marketing

www.ferndaletidewell.biz
owen@ferndaletidewell.biz

Phone: 555 014 3826
#2817 - 562 E. Harlow Ave.
Vancouver, B.C. K7P2R4 Canada
Nice to have
• - For the "FRONT" side of our business card. You can separate or re-arrange with our logo components (icon, logo,slogan). It does not have to be together.

Also our company legal name is rather long so arrange or organize the name in a way to make it shorter. Your experience and creativity will have to come in play.
Should not have
• should not have other colors beside logo color and black text (2 colors). Also nothing Three dimensional

```html
<!DOCTYPE html>
<html lang="en">
<head>
<meta charset="utf-8">
<title>Tidewell Press — Business Card</title>
<link rel="stylesheet" href="https://fonts.googleapis.com/css2?family=Open+Sans:wght@400&family=Arimo:wght@400&display=swap">
<style>
  :root {
    --brand-blue: #0079cf;
    --card-dark: #231f20;
    --text-grey: #8a8a8a;
    --rule-grey: #7d7d7d;
    --frame: #3a3a3a;
    --paper: #ffffff;
  }
  html, body {
    margin: 0;
    padding: 0;
    width: 959px;
    height: 1200px;
    overflow: hidden;
    background: var(--paper);
  }
  .canvas {
    position: relative;
    width: 959px;
    height: 1200px;
  }
  .card {
    position: absolute;
    box-sizing: border-box;
    border: 1.5px solid var(--frame);
  }
  .card--back {
    left: 0; top: 0; width: 954px; height: 584px;
    background: var(--card-dark);
  }
  .card--front {
    left: 5px; top: 616px; width: 953px; height: 583px;
    background: var(--paper);
  }
  .brand-name {
    position: absolute;
    margin: 0;
    font-family: "Open Sans", sans-serif;
    font-weight: 400;
    color: var(--brand-blue);
    white-space: nowrap;
    line-height: 1;
  }
  .card--back .brand-name--hero {
    left: 0; right: 0; top: 248px;
    text-align: center;
    font-size: 84px;
    letter-spacing: -1px;
  }
  .card--front .brand-name--hero {
    left: 70px; width: 310px; top: 283px;
    text-align: center;
    font-size: 36px;
  }
  .signature-rule {
    position: absolute;
    height: 0;
    border-top: 2px solid var(--rule-grey);
  }
  .web-address, .slogan {
    position: absolute;
    margin: 0;
    font-family: "Open Sans", sans-serif;
    color: var(--text-grey);
    white-space: nowrap;
    line-height: 1;
    text-align: right;
  }
  .web-address { font-size: 23px; letter-spacing: -0.6px; }
  .slogan { font-size: 39px; letter-spacing: -0.8px; }
  .brand-mark {
    position: absolute;
    margin: 0;
    font-family: "Open Sans", sans-serif;
    color: var(--brand-blue);
    font-size: 54px;
    line-height: 1;
    white-space: nowrap;
  }
  .card--back .signature-rule { left: 54px; width: 726px; top: 511px; }
  .card--back .web-address { right: 189px; top: 485px; }
  .card--back .slogan { right: 180px; top: 515px; }
  .card--back .brand-mark { left: 788px; top: 482px; }

  .card--front .signature-rule { left: 53px; width: 727px; top: 510px; }
  .card--front .web-address { right: 186px; top: 485px; }
  .card--front .slogan { right: 175px; top: 515px; }
  .card--front .brand-mark { left: 788px; top: 483px; }

  .divider {
    position: absolute;
    left: 379px; top: 178px;
    width: 0; height: 224px;
    border-left: 2px solid var(--rule-grey);
  }
  .contact {
    position: absolute;
    left: 416px; top: 176px;
    margin: 0;
    font-family: "Arimo", sans-serif;
    font-size: 28px;
    line-height: 33.5px;
    color: var(--text-grey);
    font-style: normal;
  }
  .contact span { display: block; white-space: nowrap; }
  .contact .gap { height: 33.5px; }
</style>
</head>
<body>
<div class="canvas">
  <section class="card card--back" aria-label="Card back">
    <p class="brand-name brand-name--hero">Tidewell Press</p>
    <p class="web-address">www.ferndaletidewell.biz</p>
    <div class="signature-rule"></div>
    <p class="slogan">Your information gateway</p>
    <p class="brand-mark">ftp</p>
  </section>

  <section class="card card--front" aria-label="Card front">
    <p class="brand-name brand-name--hero">Tidewell Press</p>
    <div class="divider"></div>
    <address class="contact">
      <span class="contact-name">Owen Marsk</span>
      <span class="contact-title">Director of Sales &amp; Marketing</span>
      <span class="contact-email">owen@ferndaletidewell.biz</span>
      <span class="gap"></span>
      <span class="contact-phone">Phone: 555 014 3826</span>
      <span class="contact-street">#2817 - 562 E. Harlow Ave.</span>
      <span class="contact-city">Vancouver, B.C. K7P2R4 Canada</span>
    </address>
    <p class="web-address">www.ferndaletidewell.biz</p>
    <div class="signature-rule"></div>
    <p class="slogan">Your information gateway</p>
    <p class="brand-mark">ftp</p>
  </section>
</div>
</body>
</html>
```